Food Service Market Place needs 3 Banner Ads for website

We need up to 3 banner ads for a new company based in Noosa called PlatrQ. We have created a Food Service Marketplace that connects the Food Service Suppliers such as growers, frozen food distributers, etc and restaurants, cafes, etc in real time. Our tag line is Connect|Save|Inspire and we would like three banners that would represent each item in the tag with a call to action to Register Now. These banners need to be designed to encourage chefs and small business owners to sign up.
Updates

Hi All, We have extended this for another 24 hours. Thanks.

Target Market(s)

Chefs, cafes, restaurants

Industry/Entity Type

Food Service

Contact Information for Business Card

Gareth Pellowe
Managing Director
garethp@platrq.com.au
1300482716
0452193078
www.platrq.com.au

Font styles to use
Sans Serif

Colors

Designer to choose colors to be used in the design.

```html
<!DOCTYPE html>
<html lang="en">
<head>
<meta charset="utf-8">
<title>PlatrQ – Connect | Save | Inspire banners</title>
<link rel="stylesheet" href="https://fonts.googleapis.com/css2?family=Montserrat:wght@800&family=Raleway:wght@400;500;700&display=swap">
<style>
  :root {
    --stage: #2e2e2e;
    --paper: #ffffff;
    --teal: #5aa8a8;
    --ink: #1e1e1e;
    --brand-ink: #4a4f52;
  }
  * { box-sizing: border-box; margin: 0; padding: 0; }
  html, body {
    width: 898px; height: 1200px; overflow: hidden;
    background: var(--stage);
    font-family: "Raleway", Arial, sans-serif;
  }
  .sheet {
    width: 898px; height: 1200px;
    padding: 37px 10px 0 11px;
    display: flex; flex-direction: column; gap: 37px;
  }
  .banner {
    position: relative;
    width: 877px; height: 351px;
    background: var(--paper);
    overflow: hidden;
  }
  .banner__media {
    position: absolute; inset: 0;
    width: 877px; height: 351px;
  }
  .banner__copy {
    position: absolute; left: 0; top: 0;
    width: 442px; height: 351px;
    display: flex; flex-direction: column; align-items: center;
    text-align: center;
  }
  .brand {
    margin-top: 30px;
    font-family: "Raleway", Arial, sans-serif;
    font-weight: 500; font-size: 44px; line-height: 1;
    color: var(--brand-ink);
  }
  .headline {
    font-family: "Raleway", Arial, sans-serif;
    font-weight: 400; color: var(--ink); line-height: 1;
  }
  .headline--hero {
    font-family: "Montserrat", Arial, sans-serif;
    font-weight: 800; color: var(--teal);
    font-size: 64px; letter-spacing: 1px;
  }
  .headline--small { font-size: 25px; }
  .row { display: flex; align-items: flex-end; gap: 8px; }
  .cta {
    display: inline-block;
    width: 125px; height: 37px; border-radius: 18px;
    background: var(--teal); color: #fff;
    font-family: "Raleway", Arial, sans-serif;
    font-weight: 700; font-size: 12px; line-height: 37px;
    text-decoration: none;
  }
  .banner--connect .headline--hero { margin-top: 75px; }
  .banner--connect .headline--small { margin-top: 15px; }
  .banner--connect .cta { margin-top: 30px; }

  .banner--save .headline--small.top { margin-top: 83px; }
  .banner--save .row { margin-top: 9px; }
  .banner--save .row .headline--small { padding-bottom: 6px; }
  .banner--save .cta { margin-top: 21px; }

  .banner--inspire .headline--small { margin-top: 87px; }
  .banner--inspire .headline--hero { margin-top: 7px; }
  .banner--inspire .cta { margin-top: 23px; }
</style>
</head>
<body>
<main class="sheet">

  <section class="banner banner--connect">
    <svg class="banner__media" viewBox="0 0 877 351" role="img" aria-label="Photo: farmer's hands holding fresh ripe tomatoes, set in a diagonal tile mosaic">
      <defs>
        <linearGradient id="connect-photo" x1="0" y1="1" x2="1" y2="0">
          <stop offset="0" stop-color="#2c2f22"/>
          <stop offset="0.5" stop-color="#7a3a26"/>
          <stop offset="1" stop-color="#3b3328"/>
        </linearGradient>
      </defs>
      <polygon points="383,351 680,0 877,0 877,351" fill="url(#connect-photo)"/>
      <g stroke="#fff" stroke-width="7" stroke-linecap="round" fill="none">
        <line x1="473" y1="351" x2="780" y2="0"/>
        <line x1="613" y1="351" x2="877" y2="60"/>
        <line x1="530" y1="230" x2="650" y2="351"/>
        <line x1="660" y1="90" x2="877" y2="300"/>
        <line x1="730" y1="0" x2="877" y2="135"/>
      </g>
    </svg>
    <div class="banner__copy">
      <p class="brand">PlatrQ</p>
      <h2 class="headline headline--hero">CONNECT</h2>
      <p class="headline headline--small">SAVE | INSPIRE</p>
      <a class="cta" href="#register">Register Now</a>
    </div>
  </section>

  <section class="banner banner--save">
    <svg class="banner__media" viewBox="0 0 877 351" role="img" aria-label="Photo: zero-waste pantry flat lay with pasta, chickpeas, kiwi, eggs, oil and a chalkboard, set in a diagonal tile mosaic">
      <defs>
        <linearGradient id="save-photo" x1="0" y1="1" x2="1" y2="0">
          <stop offset="0" stop-color="#d8c46a"/>
          <stop offset="0.45" stop-color="#e9e7e2"/>
          <stop offset="1" stop-color="#e2cfa8"/>
        </linearGradient>
      </defs>
      <polygon points="383,351 680,0 877,0 877,351" fill="url(#save-photo)"/>
      <g stroke="#fff" stroke-width="7" stroke-linecap="round" fill="none">
        <line x1="473" y1="351" x2="780" y2="0"/>
        <line x1="613" y1="351" x2="877" y2="60"/>
        <line x1="530" y1="230" x2="650" y2="351"/>
        <line x1="660" y1="90" x2="877" y2="300"/>
        <line x1="730" y1="0" x2="877" y2="135"/>
      </g>
    </svg>
    <div class="banner__copy">
      <p class="brand">PlatrQ</p>
      <p class="headline headline--small top">CONNECT</p>
      <div class="row">
        <h2 class="headline headline--hero">SAVE</h2>
        <span class="headline headline--small">| INSPIRE</span>
      </div>
      <a class="cta" href="#register">Register Now</a>
    </div>
  </section>

  <section class="banner banner--inspire">
    <svg class="banner__media" viewBox="0 0 877 351" role="img" aria-label="Photo: chef in a striped apron using a tablet on a wooden kitchen bench, set in a diagonal tile mosaic">
      <defs>
        <linearGradient id="inspire-photo" x1="0" y1="1" x2="1" y2="0">
          <stop offset="0" stop-color="#7a5536"/>
          <stop offset="0.5" stop-color="#b48a5e"/>
          <stop offset="1" stop-color="#d9cbb4"/>
        </linearGradient>
      </defs>
      <polygon points="383,351 680,0 877,0 877,351" fill="url(#inspire-photo)"/>
      <g stroke="#fff" stroke-width="7" stroke-linecap="round" fill="none">
        <line x1="473" y1="351" x2="780" y2="0"/>
        <line x1="613" y1="351" x2="877" y2="60"/>
        <line x1="530" y1="230" x2="650" y2="351"/>
        <line x1="660" y1="90" x2="877" y2="300"/>
        <line x1="730" y1="0" x2="877" y2="135"/>
      </g>
    </svg>
    <div class="banner__copy">
      <p class="brand">PlatrQ</p>
      <p class="headline headline--small">CONNECT | SAVE</p>
      <h2 class="headline headline--hero">INSPIRE</h2>
      <a class="cta" href="#register">Register Now</a>
    </div>
  </section>

</main>
</body>
</html>
```